Tree Pruning Website

We need a website for a tree Arborist, pruning company called Hollow Ridge Groundcare. We look after all types of trees, knock down trees and prune trees. Our target market is from domestic clients to government clients and everything in between.

We would like to see the use of our main colours which are orange and green

We are not looking forward in seeing a template that we have seen before but a unique template. We have designed 5 templates ourselves and we wish for the design community to take our designs to the next level.

We have also designed a template for things that **we are not** looking for (Version 4)

To make it fair for everyone, we are also not giving out any participation payments as we have had. One winner will take all of the payment!!!

I Have attached a image of the designs and a image of a tree.

We are just looking at the PSD file been developed. We have our own team who can slice the image up into a HTML format.

Target Market(s)

Everyone who needs to cut down a tree

Industry/Entity Type

Government

Requirements
Must have
• Logo on front page
A List of our services
jQuery slider on page
Phone Number on every page

```html
<!DOCTYPE html>
<html lang="en">
<head>
<meta charset="utf-8">
<title>Hollow Ridge Groundcare — Tree Surgeons</title>
<link href="https://fonts.googleapis.com/css2?family=Roboto:ital,wght@0,300;0,400;0,500;1,400&family=Montserrat:wght@500&display=swap" rel="stylesheet">
<style>
:root{
  --orange-page:#ff8a00;
  --orange-bar:#ff7400;
  --orange-deep:#e8640a;
  --green:#8cc063;
  --green-text:#5aa532;
  --sage:#ccd5c6;
  --sage-light:#e2e8de;
  --ink:#3a3a3a;
  --ink-soft:#555;
  --ghost:#e6e6e6;
  --white:#fff;
}
*{margin:0;padding:0;box-sizing:border-box}
html,body{width:1000px;height:1200px;overflow:hidden}
body{background:var(--orange-page);font-family:"Roboto",Arial,sans-serif;color:var(--ink);position:relative}
.abs{position:absolute}
.site-header{left:0;top:0;width:1000px;height:68px;background:linear-gradient(to bottom,#ff7a00,var(--orange-bar))}
.brand{left:170px;top:12px;color:var(--white);font-weight:500;font-size:21px;line-height:21px;letter-spacing:1px;text-transform:uppercase}
.header-phone{left:579px;top:30px;font-family:"Montserrat",Arial,sans-serif;font-weight:500;font-size:15px;color:#3b2a10;letter-spacing:.3px}
.header-phone span{color:var(--white)}
.main-nav{top:68px;right:0;width:1000px;height:40px}
.main-nav a{position:absolute;top:13px;font-size:11px;color:var(--white);text-decoration:none}
.page{left:129px;top:108px;width:747px;height:989px;background:var(--white)}
.hero{left:159px;top:136px;width:687px;height:307px;background:var(--sage)}
.photo{position:absolute}
.hero-photo{left:176px;top:151px;width:412px;height:275px;background:linear-gradient(160deg,#8aa0c8 0%,#9c9a5a 35%,#d9d6c6 60%,#7b7a3e 100%)}
.hero-title{right:170px;top:183px;text-align:right;font-weight:300;font-size:30px;line-height:33px;color:#444;letter-spacing:.5px}
.hero-text{right:170px;top:292px;width:225px;text-align:right;font-size:10px;line-height:17px;color:var(--ink-soft)}
.btn{position:absolute;background:var(--green);color:var(--white);font-weight:300;font-size:13px;line-height:27px;height:27px;padding:0 10px;letter-spacing:.4px}
.feature{top:468px;width:212px}
.feature h2{font-weight:300;font-size:26px;line-height:25px;color:#444;letter-spacing:.5px;margin-bottom:12px}
.feature p{font-size:9.4px;line-height:12.6px;color:var(--ink-soft)}
.services{list-style:none;margin-bottom:6px}
.services li{font-size:12px;line-height:18px;padding-left:13px;position:relative;color:#444;letter-spacing:.3px}
.services li::before{content:"";position:absolute;left:1px;top:7px;border-left:4px solid #444;border-top:2.5px solid transparent;border-bottom:2.5px solid transparent}
.section-title{left:177px;top:708px;font-weight:300;font-size:21px;color:#444;letter-spacing:.6px}
.gallery{left:159px;top:740px;width:687px;height:189px;background:var(--sage-light)}
.gallery-item{top:760px;width:153px}
.gallery-item .photo{position:relative;width:153px;height:102px}
.gallery-item p{margin-top:9px;font-size:8px;line-height:12px;color:var(--ink-soft)}
.gallery-item p b{font-weight:400;font-size:10px}
.testimonial-title{left:177px;top:952px;font-weight:300;font-size:27px;color:var(--ghost);letter-spacing:.6px}
.testimonial-lead{left:177px;top:987px;font-size:13.5px;color:var(--green-text);letter-spacing:.3px}
.testimonial-text{left:177px;top:1009px;width:650px;font-size:8.6px;line-height:12.4px;color:var(--ink-soft)}
.testimonial-author{right:188px;top:1049px;font-style:italic;font-size:9px;color:var(--ink-soft)}
.site-footer{left:129px;top:1097px;width:747px;height:61px;background:var(--orange-bar)}
.footer-address{left:175px;top:1118px;font-size:7.5px;line-height:11px;color:#ffe9d2;text-transform:uppercase}
.footer-address span{font-size:10px;text-transform:none;color:var(--white)}
.networks-label{left:675px;top:1120px;font-size:8.5px;color:var(--white)}
.network{top:1113px;width:26px;height:26px}
.footer-nav{left:129px;top:1158px;width:747px;height:30px;background:var(--orange-deep)}
.footer-nav a{position:absolute;top:10px;font-size:8px;color:var(--white);text-decoration:none}
</style>
</head>
<body>
<header class="site-header abs"></header>
<div class="brand abs">Hollow Ridge<br>Groundcare</div>
<div class="header-phone abs">CONTACT US NOW: <span>08 5550 0142</span></div>
<nav class="main-nav abs">
  <a style="left:406px">Home</a>
  <a style="left:478px">About us</a>
  <a style="left:566px">Our Services</a>
  <a style="left:674px">Get a Quote</a>
  <a style="left:779px">Contact Us</a>
</nav>

<main class="page abs"></main>

<section class="hero abs"></section>
<div class="photo hero-photo" role="img" aria-label="Looking up into the canopy of tall white-barked gum trees against a blue sky"></div>
<h1 class="hero-title abs">Lorem ipsum<br>dolorsitamet<br>consectetuer</h1>
<p class="hero-text abs">Adipiscing elit, seddiam nonummy nibheuis tincidunt ut laoreet doloremagna aliquamer dolor mag ater wisi enim ad minim enam</p>
<a class="btn" style="left:739px;top:377px">Know more</a>

<article class="feature abs" style="left:177px">
  <h2>When pruning<br>needed</h2>
  <p>Adipiscing elit, seddiam nonummy nibheuis tincidunt utlaoreet doloremagna aliquamer oremi ipsum dolor sit amet, consectetuer a dipiscingeli sed diam nonummy nibh euismod tinci dunt utao reet dolore magna aliquam erat volutpat. Utwisie nim adminim veniam, quis nostrud exerci tationu lamcorpe dolor mag ater wisi enim ad minim ena Uwisienim adminim veniam, quis nostrud exercie lamcorpe dolor mag ater wisie</p>
</article>
<a class="btn" style="left:177px;top:654px">Know more</a>

<article class="feature abs" style="left:402px">
  <h2>Why<br>need us</h2>
  <p>Adipiscing elit, seddiam nonummy nibheuis tincidunt utlaoreet doloremagna aliquamer oremi ipsum dolor sit amet, consectetuer a dipiscingeli sed diam nonummy nibh euismod tinci dunt utao reet dolore magna aliquam erat volutpat. Utwisie nim adminim veniam, quis nostrud exerci tationu lamcorpe dolor mag ater wisi enim ad minim ena Uwisienim adminim veniam, quis nostrud exercie lamcorpe dolor mag ater wisie</p>
</article>
<a class="btn" style="left:402px;top:654px">Read our testimonials</a>

<article class="feature abs" style="left:627px">
  <h2>Our<br>Services</h2>
  <ul class="services">
    <li>Tree Pruning</li>
    <li>Dangerous Tree Removal</li>
    <li>Tree Trimming</li>
    <li>Tree Shaping</li>
  </ul>
  <p>Denim adminim veniam, quis nostrud exerci tatio lamcorpe dolor mag ater wisi enim ad minim ena wisienim adminim veniam</p>
</article>
<a class="btn" style="left:628px;top:654px">Know more</a>

<h2 class="section-title abs">Our Project Gallery</h2>
<section class="gallery abs"></section>
<figure class="gallery-item abs" style="left:177px">
  <div class="photo" role="img" aria-label="Canopy of white-barked gum trees" style="background:linear-gradient(160deg,#8ea2c4,#9f9b5c 45%,#d8d4c2 70%,#7c7a40)"></div>
  <p><b>Adipiscing elit, sediam</b> nonumye tincidunt utlaoreet doremagna aliquiet ipsum dolor sit amet...</p>
</figure>
<figure class="gallery-item abs" style="left:343px">
  <div class="photo" role="img" aria-label="Arborist cutting a branch with a chainsaw" style="background:linear-gradient(135deg,#3d63a8,#5c7bb5 45%,#9a7c66 70%,#6a5a4a)"></div>
  <p><b>Adipiscing elit, sediam</b> nonumye tincidunt utlaoreet doremagna aliquiet ipsum dolor sit amet...</p>
</figure>
<figure class="gallery-item abs" style="left:510px">
  <div class="photo" role="img" aria-label="Pruned bare branches against a blue sky" style="background:linear-gradient(to bottom,#6d8fcf,#8ea9db 55%,#4e4a3a)"></div>
  <p><b>Adipiscing elit, sediam</b> nonumye tincidunt utlaoreet doremagna aliquiet ipsum dolor sit amet...</p>
</figure>
<figure class="gallery-item abs" style="left:677px">
  <div class="photo" role="img" aria-label="Arborist in a lift bucket beside a large trunk" style="background:linear-gradient(90deg,#8a7a62,#7a6c58 30%,#5d7fb8 50%,#6f8fc6 80%,#d9dde4)"></div>
  <p><b>Adipiscing elit, sediam</b> nonumye tincidunt utlaoreet doremagna aliquiet ipsum dolor sit amet...</p>
</figure>

<h2 class="testimonial-title abs">What do our clients say about us...</h2>
<p class="testimonial-lead abs">They have done a great clean job, they deserve to be called the real professionals...</p>
<p class="testimonial-text abs">Adipiscing elit, seddiam nonummy nibheuis tincidunt utlaoreet doloremagna aliquamer oremi ipsum dolor sit amet, consectetuer a dipiscingeli sed diam nonummy nibh euismod tinci dunt utao reet dolore magna aliquam erat volutpat twisienim adminim veniam, quis nostrud exerci tatioadm amcorpe dolor mag ater wisi enim ad minim enawi sienim adminim veniam, quis nostrud exercie lamcorpe dolor mag ater wisie...</p>
<p class="testimonial-author abs">Daniel Osmond, CA</p>

<footer class="site-footer abs"></footer>
<p class="footer-address abs">41 Marlow Street, Fernbrook, WA 6999<br>Contact us now: <span>08 5550 0142</span> &nbsp;Fax: <span>08 5550 0199</span></p>
<p class="networks-label abs">Our Networks</p>
<svg class="network abs" style="left:749px" viewBox="0 0 26 26" aria-label="Social network"><rect width="26" height="26" fill="#d9432f"/></svg>
<svg class="network abs" style="left:785px" viewBox="0 0 26 26" aria-label="Social network"><rect width="26" height="26" fill="#3b5a9a"/></svg>
<svg class="network abs" style="left:821px" viewBox="0 0 26 26" aria-label="Social network"><rect width="26" height="26" fill="#3fb3e6"/></svg>
<nav class="footer-nav abs">
  <a style="left:28px">Home</a>
  <a style="left:68px">About us</a>
  <a style="left:121px">Our Services</a>
  <a style="left:188px">Get a Quote</a>
  <a style="left:252px">Contact Us</a>
  <a style="left:414px">Tree Pruning</a>
  <a style="left:479px">Dangerous Tree Removal</a>
  <a style="left:593px">Tree Trimming</a>
  <a style="left:667px">Tree Shaping</a>
</nav>
</body>
</html>
```